Letterhead for small civil engineer company

We need bold and modern design for company letterhead in MS word. It needs to have company logo and company info. Somewhere in the upper right part of document needs to be space for "recever" and the documents starts with, example, "SUBJECT: CIVIL ENGINEER LETTERHEAD".

in the bottom part of document needs to be signature and date.

Company info: Vrelon d.o.o., Dravunja 47, Lastovac (Općina Brenovo), OIB 47392615084, www.vrelon.hr, info@vrelon.hr

Email of document sender needs to be somewhere if document, exapmle xyz@vrelo.hr

Target Market(s)

Civil engineer company and projects

Industry/Entity Type

Civil engineer

Font styles to use
Serif

Colors
F0912C
F2A743
F7CA91
FBE8D2
FDF5EE

Requirements
Must have
• Company logo and company info
Nice to have
• Moder and clean design
Should not have
• Too much details

```html
<!DOCTYPE html>
<html lang="en">
<head>
<meta charset="utf-8">
<title>Vrelon d.o.o. — Letterhead</title>
<link rel="stylesheet" href="https://fonts.googleapis.com/css2?family=Nunito+Sans:wght@400;600;700&display=swap">
<style>
  :root {
    --orange: #F0912C;
    --orange-faint: #FBE8D2;
    --ink: #2e2e2e;
    --ink-soft: #4a4a4a;
    --edge: #555555;
    --backdrop: #6b6b6b;
    --paper: #ffffff;
  }
  * { margin: 0; padding: 0; box-sizing: border-box; }
  html, body {
    width: 799px; height: 1200px; overflow: hidden;
    background: var(--backdrop);
    font-family: "Nunito Sans", Arial, sans-serif;
  }
  .edges { position: absolute; left: 0; top: 0; }
  .letterhead {
    position: absolute; left: 50px; top: 105px;
    width: 700px; height: 990px;
    background: var(--paper);
    color: var(--ink);
  }
  .brand {
    position: absolute; left: 70px; top: 104px;
    display: flex; align-items: center; gap: 10px;
  }
  .brand-square {
    width: 18px; height: 18px; border: 2px solid var(--edge);
  }
  .brand-name {
    font-size: 26px; font-weight: 700; letter-spacing: 2px;
    color: var(--orange); line-height: 1;
  }
  .subject {
    position: absolute; left: 62px; top: 197px;
    font-size: 18px; font-weight: 600; letter-spacing: 0.6px;
  }
  .salutation {
    position: absolute; left: 62px; top: 283px;
    font-size: 20px; font-weight: 600;
  }
  .body-copy {
    position: absolute; left: 62px; top: 327px; width: 562px;
    font-size: 12.6px; line-height: 15.8px; text-align: justify;
    color: var(--ink);
  }
  .body-copy p + p { margin-top: 26px; }
  .watermark {
    position: absolute; left: 120px; top: 470px; width: 460px;
    text-align: center;
    font-size: 50px; font-weight: 700; letter-spacing: 6px;
    color: var(--orange-faint); opacity: 0.5;
  }
  .signature {
    position: absolute; left: 62px; top: 702px;
    width: 124px; height: 40px;
    background: linear-gradient(90deg, #f0f0f0, #f8f8f8);
    border-radius: 4px;
  }
  .sign-date {
    position: absolute; left: 62px; top: 758px;
    font-size: 16px; font-weight: 600; color: var(--ink-soft);
  }
  .footer-contact {
    position: absolute; left: 62px; top: 940px;
    font-size: 14.4px; color: var(--orange); line-height: 24px;
  }
  .footer-contact li, .footer-legal li { list-style: none; display: flex; align-items: center; gap: 8px; }
  .footer-legal {
    position: absolute; right: 66px; top: 940px;
    font-size: 14.4px; line-height: 24px; color: var(--ink-soft);
    text-align: right;
  }
  .footer-legal li { justify-content: flex-end; }
  .oib { font-weight: 700; margin-right: 20px; }
  .icon { flex: none; }
</style>
</head>
<body>
  <svg class="edges" width="799" height="1200" viewBox="0 0 799 1200" aria-hidden="true">
    <rect x="36" y="105" width="14" height="486" fill="var(--edge)"/>
    <rect x="36" y="609" width="14" height="498" fill="var(--orange)"/>
    <polygon points="36,600 50,588 50,612" fill="var(--paper)"/>
    <rect x="36" y="1095" width="344" height="12" fill="var(--orange)"/>
    <rect x="406" y="1095" width="344" height="12" fill="var(--edge)"/>
    <polygon points="380,1095 406,1095 393,1107" fill="var(--paper)"/>
  </svg>

  <main class="letterhead">
    <header class="brand">
      <span class="brand-square"></span>
      <span class="brand-name">VRELON</span>
    </header>

    <h1 class="subject">SUBJECT</h1>
    <h2 class="salutation">Dear Sir/Madam,</h2>

    <div class="watermark" aria-hidden="true">VRELON</div>

    <section class="body-copy">
      <p>Lorem Ipsum is simply dummy text of the printing and typesetting industry. Lorem Ipsum has been the industry's standard dummy text ever since the 1500s, when an unknown printertook a galley of type and scrambled it to make a type specimen book.It has survived not only five centuries, but also the leap into electronic typesetting, remaining essentially unchanged. Itto was popularised in the 1960s with the release of Typeline sheets containing Lorem Ipsum cgv passages, and more recently with desktop publishing software like Quillset Pressmark including versions of Lorem Ipsum.</p>
      <p>Contrary to popular belief, Lorem Ipsum is not simply random text. It has roots in a piece of classical Latin literature from 45 BC, making it over 2000 years old.</p>
      <p>Tomas Verhale, a Latin professor at Marrowfield College in Ostria, looked up one of the more obscure Latin words, consectetur, from a Lorem Ipsum passage, and going through the cites of the word in classical literature, discovered the undoubtable source. Lorem Ipsum comes from sections</p>
      <p>Contrary to popular belief, Lorem Ipsum is not simply random text. It has roots in a piece of classical Latin literature from 45 BC, making it over 2000 years old.</p>
    </section>

    <div class="signature" role="img" aria-label="Handwritten signature of the sender"></div>
    <p class="sign-date">14/12/2024</p>

    <ul class="footer-contact">
      <li>
        <svg class="icon" width="12" height="9" viewBox="0 0 12 9"><rect width="12" height="9" rx="1" fill="var(--orange)"/><polyline points="1,1.5 6,5 11,1.5" fill="none" stroke="#fff" stroke-width="1.2"/></svg>
        info@vrelon.hr
      </li>
      <li>
        <svg class="icon" width="12" height="11" viewBox="0 0 12 11"><circle cx="6" cy="3" r="2.6" fill="var(--orange)"/><path d="M1 11 Q6 4 11 11 Z" fill="var(--orange)"/></svg>
        Vrelon d.o.o., Dravunja 47, Lastovac (Općina Brenovo)
      </li>
    </ul>

    <ul class="footer-legal">
      <li class="oib">OIB 47392615084</li>
      <li>
        www.vrelon.hr
        <svg class="icon" width="11" height="11" viewBox="0 0 12 12"><circle cx="6" cy="6" r="5.2" fill="none" stroke="var(--ink-soft)" stroke-width="1.2"/><ellipse cx="6" cy="6" rx="2.2" ry="5.2" fill="none" stroke="var(--ink-soft)" stroke-width="1"/><line x1="1" y1="6" x2="11" y2="6" stroke="var(--ink-soft)" stroke-width="1"/></svg>
      </li>
    </ul>
  </main>
</body>
</html>
```